July 4th Postcard to existing clients

5x7 postcard wishing our clients happy 4th of July. Card should read on the back "Thank You For Being A Valued Client!. Stay Safe And Enjoy Your Independence Day Celebrations!"

Patriotic theme with fireworks is ideal. We are a law firm so should still have a feel of professionalism while still being fun since it is for a fun holiday.

```html
<!DOCTYPE html>
<html lang="en">
<head>
<meta charset="utf-8">
<title>Marlow Law – Fourth of July Postcard</title>
<link rel="stylesheet" href="https://fonts.googleapis.com/css2?family=Exo+2:ital,wght@1,700;1,900&family=Montserrat:wght@300;400&family=Questrial&display=swap">
<style>
  :root {
    --stage: #000000;
    --navy-deep: #0c1d5c;
    --navy: #1a3288;
    --royal: #2c4aa8;
    --sky-glow: #3f5fb8;
    --flag-red: #e0261c;
    --white: #ffffff;
    --star-navy: #1d2f7a;
    --firm-grey: #6d6d72;
    --address-blue: #2f4da0;
    --stamp-line: #c9c9c9;
    --web-border: #6e8ee0;
  }
  * { margin: 0; padding: 0; box-sizing: border-box; }
  html, body {
    width: 881px; height: 1200px; overflow: hidden;
    background: var(--stage);
  }
  .postcard {
    position: absolute; left: 66px; width: 749px; height: 535px;
    overflow: hidden; background: var(--white);
  }
  .postcard--front { top: 56px; }
  .postcard--back { top: 606px; }

  .night-scene {
    position: absolute; inset: 0;
    background:
      radial-gradient(ellipse at 25% 15%, rgba(210,180,120,0.35), transparent 35%),
      radial-gradient(ellipse at 80% 20%, rgba(170,90,200,0.35), transparent 30%),
      radial-gradient(ellipse at 50% 65%, rgba(160,170,220,0.35), transparent 45%),
      linear-gradient(180deg, var(--navy) 0%, var(--royal) 55%, var(--sky-glow) 100%);
  }
  .postcard--back .night-scene { right: auto; width: 400px; }

  .front-title {
    position: absolute; left: 0; right: 0; top: 48px;
    text-align: center; color: var(--white);
    font-family: "Exo 2", sans-serif; font-style: italic; font-weight: 900;
    text-transform: uppercase; line-height: 1;
  }
  .front-title span { display: block; }
  .front-title .happy { font-size: 46px; }
  .front-title .fourth { font-size: 64px; margin-top: 2px; }
  .front-title .of { font-size: 32px; letter-spacing: 2px; margin-top: 4px; }
  .front-title .july { font-size: 88px; margin-top: 0; }
  .front-title .star-row { font-size: 34px; letter-spacing: 4px; font-style: normal; margin-top: 8px; }

  .front-curve { position: absolute; inset: 0; }

  .firm-name {
    font-family: "Montserrat", sans-serif; font-weight: 300;
    color: var(--firm-grey); letter-spacing: 1.5px; text-transform: uppercase;
  }
  .front-firm {
    position: absolute; left: 0; right: 0; top: 478px;
    text-align: center; font-size: 21px;
  }

  .back-wave { position: absolute; inset: 0; }

  .thanks {
    position: absolute; left: 14px; width: 300px; top: 82px;
    text-align: center; color: var(--white);
    font-family: "Exo 2", sans-serif; font-style: italic; font-weight: 700;
    font-size: 41px; line-height: 53px;
  }
  .wishes {
    position: absolute; left: 14px; width: 300px; top: 318px;
    text-align: center; color: var(--white);
    font-family: "Questrial", sans-serif; font-size: 19px; line-height: 26px;
  }
  .website {
    position: absolute; left: 60px; top: 478px; width: 210px; height: 28px;
    border: 1px solid var(--web-border);
    color: var(--white); font-family: "Questrial", sans-serif;
    font-size: 18px; line-height: 26px; text-align: center;
  }
  .back-firm { position: absolute; left: 426px; top: 72px; font-size: 20px; }
  .address {
    position: absolute; left: 428px; top: 103px;
    font-family: "Montserrat", sans-serif; font-size: 11.5px; line-height: 15px;
    color: var(--address-blue);
  }
  .stamp-box {
    position: absolute; left: 627px; top: 51px; width: 79px; height: 79px;
    border: 1px solid var(--stamp-line);
  }
</style>
</head>
<body>

<section class="postcard postcard--front">
  <div class="night-scene" role="img" aria-label="Night sky with fireworks bursting above a row of waving American flags"></div>

  <h1 class="front-title">
    <span class="happy">★ Happy ★</span>
    <span class="fourth">Fourth</span>
    <span class="of">★★★of★★★</span>
    <span class="july">July</span>
    <span class="star-row">★★★★★★★</span>
  </h1>

  <svg class="front-curve" viewBox="0 0 749 535" width="749" height="535" aria-hidden="true">
    <defs>
      <path id="front-star-track" d="M-10 512 Q374 348 760 506"/>
    </defs>
    <path d="M0 480 Q374 308 749 474 L749 535 L0 535 Z" fill="var(--flag-red)"/>
    <path d="M0 490 Q374 322 749 484 L749 535 L0 535 Z" fill="var(--white)"/>
    <text font-size="12" fill="var(--star-navy)" letter-spacing="17">
      <textPath href="#front-star-track">★★★★★★★★★★★★★★★★★★★★★★★★★★★★★★★★★★★★★★★★★★</textPath>
    </text>
  </svg>

  <p class="firm-name front-firm">Marlow Law</p>
</section>

<section class="postcard postcard--back">
  <div class="night-scene" role="img" aria-label="Fireworks over a night sky with American flags waving below"></div>

  <svg class="back-wave" viewBox="0 0 749 535" width="749" height="535" aria-hidden="true">
    <defs>
      <path id="back-star-track" d="M396 0 C419 80 354 180 364 300 C372 420 409 470 409 535"/>
    </defs>
    <path d="M372 0 C395 80 330 180 340 300 C348 420 385 470 385 535 L749 535 L749 0 Z" fill="var(--white)"/>
    <path d="M383 0 C406 80 341 180 351 300 C359 420 396 470 396 535" fill="none" stroke="var(--flag-red)" stroke-width="7"/>
    <text font-size="8" fill="var(--star-navy)" letter-spacing="2">
      <textPath href="#back-star-track">★★★★★★★★★★★★★★★★★★★★★★★★★★★★★★★★★★★★★★★★★★★★★★★★★★★★★★★★★★</textPath>
    </text>
  </svg>

  <h2 class="thanks">Thank You<br>For Being<br>A Valued<br>Client!.</h2>
  <p class="wishes">Stay Safe and Enjoy Your<br>Independence Day<br>Celebrations!</p>
  <p class="website">www.marlowlaw.com</p>

  <p class="firm-name back-firm">Marlow Law</p>
  <p class="address">1480 W Cedarbrook<br>St Springfield, MO 65807</p>
  <div class="stamp-box" aria-label="Stamp area"></div>
</section>

</body>
</html>
```